Create a website in Wordpress for an interior design company

Create a website for our interior design company 'Roomora'

-Color preferences - Neutral and warm colors. Nothing too bright
-Aesthetic: Modern, Minimalist, Classic, Mature, Luxury
-Mission Statement: Transforming homes into personalized dream spaces through exceptional interior design, meticulous attention to detail, and a touch of the unexpected.
-Brand Values: innovation, creativity, passion and sustainability

Examples: https://www.lenamarchwoodinteriors.com.au/
https://www.tidecraftstudio.com/

About
Portfolio
Inquire page

```html
<!DOCTYPE html>
<html lang="en">
<head>
<meta charset="utf-8">
<title>Roomora — Modern Interior Design Company</title>
<link href="https://fonts.googleapis.com/css2?family=Poppins:wght@300;400;500;600;700&display=swap" rel="stylesheet">
<style>
:root{
  --tan:#b89f7f;
  --tan-dark:#a58b69;
  --cream:#f2e6d8;
  --paper:#f5f5f5;
  --ink:#111111;
  --text:#3a3a3a;
  --white:#ffffff;
  --rule:#3b3b3b;
}
*{box-sizing:border-box;margin:0;padding:0}
html,body{width:1200px;height:3704px;overflow:hidden}
body{font-family:'Poppins',sans-serif;color:var(--ink);background:var(--white);position:relative}
.abs{position:absolute}
.photo{position:absolute}
.btn{position:absolute;display:flex;align-items:center;justify-content:center;gap:12px;border-radius:40px;font-weight:500;text-transform:uppercase}
.btn .dot{width:19px;height:19px;border-radius:50%;display:inline-flex;align-items:center;justify-content:center}
.btn-tan{background:var(--tan);color:var(--white);font-size:13px}
.btn-tan .dot{background:var(--white)}
.btn-white{background:var(--white);color:var(--ink)}
.btn-white .dot{background:var(--tan)}

/* header */
.site-header{position:absolute;left:0;top:0;width:1200px;height:105px;background:var(--white)}
.brand{position:absolute;left:68px;top:30px;font-size:38px;font-weight:500;letter-spacing:-0.5px}
.main-nav a{position:absolute;top:47px;font-size:13px;color:var(--ink);text-decoration:none}
.main-nav a.active{font-weight:500}
.main-nav a.active::after{content:"";position:absolute;left:0;right:0;bottom:-9px;height:2px;background:var(--ink)}
.inquire-btn{left:1018px;top:34px;width:119px;height:37px;font-size:13px}

/* hero */
.hero-panel{position:absolute;left:0;top:105px;width:555px;height:653px;background:var(--tan)}
.hero-photo{left:555px;top:105px;width:645px;height:653px;background:linear-gradient(160deg,#ece7df 0%,#d9cdbd 45%,#8a5e3a 75%,#cfc3b2 100%)}
.hero-kicker{position:absolute;left:72px;top:236px;font-size:34px;color:var(--white);font-weight:400}
.hero-line{position:absolute;left:68px;font-weight:600;text-transform:uppercase}
.hero-modern{top:294px;font-size:48px;color:var(--white)}
.hero-interior{top:350px;font-size:92px;color:var(--ink);font-weight:700;letter-spacing:-1px}
.hero-company{top:448px;font-size:48px;color:var(--white)}
.hero-cta{left:68px;top:537px;width:239px;height:72px;font-size:19px;font-weight:600}
.slider-dots{position:absolute;left:254px;top:700px;display:flex;gap:3px}
.slider-dots span{width:11px;height:11px;border-radius:50%;background:#d8cab7}
.slider-dots span:first-child{background:var(--white)}

/* about */
.about{position:absolute;left:0;top:758px;width:1200px;height:627px;background:var(--paper)}
.section-title{font-size:48px;font-weight:500;color:var(--ink)}
.about-title{position:absolute;left:109px;top:100px}
.about-kicker{position:absolute;left:109px;top:158px;font-size:14px;color:var(--tan);display:flex;align-items:center;gap:8px}
.about-kicker i{display:block;width:64px;height:1px;background:var(--tan);position:relative}
.about-kicker i::before{content:"";position:absolute;left:-3px;top:-3px;width:7px;height:7px;border-radius:50%;background:var(--tan)}
.about-text{position:absolute;left:109px;top:206px;width:473px;font-size:14px;line-height:26.6px;color:var(--text);text-align:justify}
.about-btn{left:109px;top:427px;width:171px;height:52px}
.about-photo-back{left:647px;top:61px;width:413px;height:420px;background:linear-gradient(135deg,#8a6a4a,#4a3a2c 55%,#b6a38a)}
.about-photo-frame{position:absolute;left:722px;top:127px;width:413px;height:422px;background:var(--white)}
.about-photo-front{left:8px;top:9px;width:397px;height:404px;background:linear-gradient(180deg,#f4f2ef 0%,#d7c2a2 40%,#eeeeee 65%,#7a6a5c 100%)}

/* features */
.features{position:absolute;left:0;top:1385px;width:1200px;height:348px;background:var(--tan);border-top:2px solid var(--rule);border-bottom:2px solid var(--rule)}
.feature{position:absolute;top:67px;width:300px;text-align:center;color:var(--white)}
.feature-icon{width:84px;height:84px;margin:0 auto;background:var(--white);border:1px solid #8a7258;display:flex;align-items:center;justify-content:center}
.feature h3{margin-top:26px;font-size:20px;font-weight:500;text-transform:uppercase;letter-spacing:0.2px}
.feature p{margin:12px auto 0;width:260px;font-size:13.5px;line-height:24px;font-weight:300}

/* portfolio */
.portfolio-title{position:absolute;left:0;width:1200px;top:1833px;text-align:center}
.portfolio-kicker{position:absolute;left:0;width:1200px;top:1889px;display:flex;justify-content:center;align-items:center;gap:10px;font-size:14px;color:var(--tan)}
.portfolio-kicker i{display:block;width:70px;height:1px;background:var(--tan);position:relative}
.portfolio-kicker i.l::after,.portfolio-kicker i.r::before{content:"";position:absolute;top:-3px;width:7px;height:7px;border-radius:50%;background:var(--tan)}
.portfolio-kicker i.l::after{right:-3px}
.portfolio-kicker i.r::before{left:-3px}
.tile{position:absolute;border-radius:2px}
.view-btn{left:514px;top:2629px;width:171px;height:52px}

/* inquire */
.inquire-photo{left:0;top:2760px;width:626px;height:468px;background:linear-gradient(170deg,#f1ede6 0%,#cfc2b0 40%,#6e4a30 70%,#b9ab99 100%)}
.inquire-panel{position:absolute;left:626px;top:2760px;width:574px;height:468px;background:var(--tan)}
.inquire-heading{position:absolute;left:0;width:574px;top:100px;text-align:center;color:var(--white);font-size:64px;font-weight:500;line-height:78px}
.inquire-cta{left:113px;top:294px;width:305px;height:52px;font-size:13.5px;font-weight:600;text-transform:uppercase}

/* contact area */
.contact-area{position:absolute;left:0;top:3228px;width:1200px;height:412px;background:var(--cream)}
.newsletter{position:absolute;left:240px;top:97px;width:718px;height:97px;border-radius:50px;background:var(--tan);box-shadow:6px 0 0 var(--tan-dark)}
.newsletter h2{position:absolute;left:33px;top:29px;font-size:28px;font-weight:500;color:var(--white)}
.newsletter-field{position:absolute;left:369px;top:33px;width:309px;height:32px;border-radius:20px;background:var(--white)}
.newsletter-field span{position:absolute;left:17px;top:9px;font-size:10px;color:#777}
.newsletter-btn{position:absolute;right:0;top:0;width:93px;height:32px;border-radius:20px;background:var(--tan-dark);color:var(--white);font-size:13px;font-weight:600;display:flex;align-items:center;justify-content:center}
.contact-item{position:absolute;top:248px;display:flex;gap:14px;align-items:flex-start}
.contact-icon{width:30px;height:30px;border-radius:3px;background:var(--ink);display:flex;align-items:center;justify-content:center;margin-top:2px}
.contact-item strong{display:block;font-size:13px;font-weight:600;text-transform:uppercase}
.contact-item span{display:block;font-size:14px;line-height:18px}
.contact-rule{position:absolute;left:67px;top:328px;width:1066px;height:1px;background:#bcae9d}
.footer-nav a{position:absolute;top:355px;font-size:13.5px;color:var(--ink);text-decoration:none;font-weight:500}
.footer-nav a:first-child{font-weight:600}

/* bottom bar */
.copyright-bar{position:absolute;left:0;top:3640px;width:1200px;height:64px;background:var(--ink)}
.copyright-bar p{position:absolute;left:67px;top:24px;font-size:12px;color:var(--white)}
.social-links{position:absolute;right:63px;top:20px;display:flex;gap:6px}
.social-links span{width:26px;height:26px;border:1.5px solid var(--white);border-radius:3px;display:block;position:relative}
.social-links span::after{content:"";position:absolute;left:6px;top:6px;width:11px;height:11px;background:var(--white);border-radius:2px}
</style>
</head>
<body>

<header class="site-header">
  <div class="brand">Roomora</div>
  <nav class="main-nav">
    <a class="active" style="left:555px">HOME</a>
    <a style="left:660px">ABOUT US</a>
    <a style="left:787px">PORTFOLIO</a>
    <a style="left:920px">CONTACT</a>
  </nav>
  <div class="btn btn-tan inquire-btn">Inquire</div>
</header>

<section class="hero">
  <div class="hero-panel">
    <p class="hero-kicker">Welcome To Roomora</p>
    <p class="hero-line hero-modern">Modern</p>
    <p class="hero-line hero-interior">Interior</p>
    <p class="hero-line hero-company">Design Company</p>
    <div class="btn btn-white hero-cta">Get Started <span class="dot"><svg width="8" height="8" viewBox="0 0 8 8"><path d="M2 1l4 3-4 3z" fill="#fff"/></svg></span></div>
    <div class="slider-dots" style="top:595px"><span></span><span></span><span></span><span></span></div>
  </div>
  <div class="photo hero-photo" role="img" aria-label="Living room with panelled walls, wooden door, leather bench and television console"></div>
</section>

<section class="about">
  <h2 class="section-title about-title">About Us</h2>
  <p class="about-kicker">WHO WE ARE <i></i></p>
  <p class="about-text">Lorem ipsum dolor sit amet, consectetur adipiscing elit. Aliquam at fermentum erat. Suspendisse convallis ultrices efficitur. Suspendisse potenti. Etiam ullamcorper ipsum eu felis feugiat, id fermentum justo rhoncus. Vestibulum laoreet placerat vehicula. Fusce ligula mi, tempor id maximus a, tempus non mi. Vestibulum ante ipsum primis in faucibus orci luctus et ultrices posuere cubilia curae; Aenean scelerisque dolor in urna condimentum volutpat.</p>
  <div class="btn btn-tan about-btn">Read More <span class="dot"><svg width="8" height="8" viewBox="0 0 8 8"><path d="M2 1l4 3-4 3z" fill="#b89f7f"/></svg></span></div>
  <div class="photo about-photo-back" role="img" aria-label="Room with wooden shelving and curtains"></div>
  <div class="about-photo-frame">
    <div class="photo about-photo-front" role="img" aria-label="Bright lounge with white sofa and wood-panelled wall"></div>
  </div>
</section>

<section class="features">
  <div class="feature" style="left:100px">
    <div class="feature-icon"><svg width="38" height="38" viewBox="0 0 38 38"><path d="M14 6h10l-3 5h-4z" fill="#111"/><path d="M17 11h4c8 4 11 11 11 16 0 5-4 7-13 7S6 32 6 27c0-5 3-12 11-16z" fill="#111"/><text x="19" y="29" font-family="Poppins,sans-serif" font-size="12" font-weight="700" fill="#fff" text-anchor="middle">$</text></svg></div>
    <h3>Resonable Prices</h3>
    <p>Lorem ipsum dolor sit amet, consec tetur adipiscing elit. Aliquam at fer mentum erat.</p>
  </div>
  <div class="feature" style="left:449px">
    <div class="feature-icon"><svg width="40" height="40" viewBox="0 0 40 40"><rect x="5" y="7" width="30" height="26" fill="none" stroke="#111" stroke-width="3"/><rect x="9" y="11" width="4" height="18" fill="#111"/><circle cx="23" cy="20" r="6" fill="none" stroke="#111" stroke-width="3"/><circle cx="23" cy="20" r="2" fill="#111"/></svg></div>
    <h3>Exclusive Design</h3>
    <p>Lorem ipsum dolor sit amet, consec tetur adipiscing elit. Aliquam at fer mentum erat.</p>
  </div>
  <div class="feature" style="left:801px">
    <div class="feature-icon"><svg width="46" height="40" viewBox="0 0 46 40"><circle cx="23" cy="12" r="6" fill="#111"/><circle cx="11" cy="15" r="5" fill="#111"/><circle cx="35" cy="15" r="5" fill="#111"/><path d="M13 34c0-8 4-13 10-13s10 5 10 13z" fill="#111"/><path d="M2 32c0-6 3-10 9-10 2 0 3 1 4 1-3 3-4 6-4 9z" fill="#111"/><path d="M44 32c0-6-3-10-9-10-2 0-3 1-4 1 3 3 4 6 4 9z" fill="#111"/></svg></div>
    <h3>Professional Team</h3>
    <p>Lorem ipsum dolor sit amet, consec tetur adipiscing elit. Aliquam at fer mentum erat.</p>
  </div>
</section>

<section class="portfolio">
  <h2 class="section-title portfolio-title">Our Portfolio</h2>
  <p class="portfolio-kicker"><i class="l"></i>PROJECTS<i class="r"></i></p>
  <div class="tile" role="img" aria-label="Living room with sofa, artwork and city-view windows" style="left:69px;top:1957px;width:525px;height:301px;background:linear-gradient(135deg,#c9903f,#5a4a40 50%,#2d2a30)"></div>
  <div class="tile" role="img" aria-label="White kitchen with island and bar stools" style="left:609px;top:1957px;width:525px;height:301px;background:linear-gradient(180deg,#f2f2f0,#dcdcd8 60%,#6b4a30)"></div>
  <div class="tile" role="img" aria-label="Dining area with black chairs and pendant lamps" style="left:69px;top:2272px;width:344px;height:301px;background:linear-gradient(160deg,#5c5a57,#e7e5e1 55%,#cfcac2)"></div>
  <div class="tile" role="img" aria-label="Bathroom vanity with wooden cabinets and mirror" style="left:428px;top:2272px;width:344px;height:301px;background:linear-gradient(180deg,#d8d2ca,#a9643a 65%,#e6e0d8)"></div>
  <div class="tile" role="img" aria-label="Bathroom with marble counter and glass shower" style="left:789px;top:2272px;width:344px;height:301px;background:linear-gradient(160deg,#a58b5c,#cfcac4 45%,#c89a3a)"></div>
  <div class="btn btn-tan view-btn">View More <span class="dot"><svg width="8" height="8" viewBox="0 0 8 8"><path d="M2 1l4 3-4 3z" fill="#b89f7f"/></svg></span></div>
</section>

<section class="inquire">
  <div class="photo inquire-photo" role="img" aria-label="Classic living room with chandelier, wooden cabinetry and lounge chairs"></div>
  <div class="inquire-panel">
    <h2 class="inquire-heading">Inquire<br>with Roomora</h2>
    <div class="btn btn-white inquire-cta">Schedule Your Discovery Call <span class="dot" style="width:14px;height:14px"><svg width="6" height="6" viewBox="0 0 8 8"><path d="M2 1l4 3-4 3z" fill="#fff"/></svg></span></div>
  </div>
</section>

<section class="contact-area">
  <div class="newsletter">
    <h2>Our Newsletter Sign Up</h2>
    <div class="newsletter-field"><span>Enter Email Address</span><div class="newsletter-btn">SIGNUP</div></div>
  </div>
  <div class="contact-item" style="left:229px">
    <div class="contact-icon"><svg width="14" height="14" viewBox="0 0 14 14"><path d="M3 1l2 3-1 2c1 2 2 3 4 4l2-1 3 2-1 2C6 13 1 8 1 2z" fill="#fff"/></svg></div>
    <div><strong>Call Us</strong><span>8012 345 6789</span></div>
  </div>
  <div class="contact-item" style="left:423px">
    <div class="contact-icon"><svg width="14" height="10" viewBox="0 0 14 10"><rect width="14" height="10" fill="#fff"/><path d="M0 0l7 6 7-6" fill="none" stroke="#111" stroke-width="1.3"/></svg></div>
    <div><strong>Email Us</strong><span>info@websitename.com</span></div>
  </div>
  <div class="contact-item" style="left:702px">
    <div class="contact-icon"><svg width="12" height="16" viewBox="0 0 12 16"><path d="M6 0a6 6 0 0 1 6 6c0 4-6 10-6 10S0 10 0 6a6 6 0 0 1 6-6z" fill="#fff"/><circle cx="6" cy="6" r="2" fill="#111"/></svg></div>
    <div><span>Address line Dummy Here</span><span>Address line Here</span></div>
  </div>
  <div class="contact-rule"></div>
  <nav class="footer-nav">
    <a style="left:384px">HOME</a>
    <a style="left:489px">ABOUT US</a>
    <a style="left:616px">PORTFOLIO</a>
    <a style="left:749px">CONTACT</a>
  </nav>
</section>

<footer class="copyright-bar">
  <p>Copyright © 2024 All Rights Reserved By Comapny Name</p>
  <div class="social-links"><span></span><span></span><span></span><span></span></div>
</footer>

</body>
</html>
```